Lumora business card for a plastic surgeon

we need a business card for plastic surgeons that work on a clinic called LUMORA.
we want a clean design and the following informations: name of the doctor, doctor's registration number (called CRM), telephone, address, facebook, instagram.
Colors: white, blue tones, light brown/ coffee

facebook and instagram: lumoraesteticaclinica

Industry/Entity Type

Business

Contact Information for Business Card

clean design

Font styles to use
Serif
Sans Serif
Other font styles liked:
• helvetica light

Colors
cee9f5
85cae6
85abd2
3276b5
cfeae6
cedeed
eaf1f7

Requirements
Must have
• doctor's name
• identification number (called CRM)
• contact (phone, facebook, instagram, address)

```html
<!DOCTYPE html>
<html lang="pt">
<head>
<meta charset="utf-8">
<title>Lumora – Business Card</title>
<link rel="stylesheet" href="https://fonts.googleapis.com/css2?family=Open+Sans:wght@400;600&display=swap">
<style>
  :root {
    --backdrop: #2b2b2d;
    --card: #121213;
    --card-edge: #1c1c1e;
    --accent: #19c1e2;
    --ink: #f2f2f2;
    --rule: #232325;
  }
  * { box-sizing: border-box; margin: 0; padding: 0; }
  html, body { width: 1200px; height: 900px; overflow: hidden; }
  body {
    background: var(--backdrop);
    font-family: "Open Sans", Arial, sans-serif;
    display: flex;
    align-items: center;
    justify-content: center;
    gap: 48px;
  }
  .card {
    width: 500px;
    height: 286px;
    background: var(--card);
    border: 1px solid var(--card-edge);
    border-radius: 18px;
    position: relative;
    overflow: hidden;
    box-shadow: 0 18px 40px rgba(0,0,0,.45);
  }
  /* front: contact side */
  .card--contact { display: flex; }
  .mark-panel {
    width: 46%;
    display: flex;
    flex-direction: column;
    align-items: center;
    justify-content: center;
    gap: 14px;
    border-right: 1px solid var(--rule);
  }
  .mark-dot {
    width: 64px; height: 64px;
    border-radius: 50%;
    background: var(--accent);
  }
  .mark-name {
    color: var(--accent);
    font-weight: 600;
    font-size: 22px;
    letter-spacing: 4px;
  }
  .details {
    flex: 1;
    padding: 48px 24px 0 26px;
    color: var(--ink);
    font-size: 12.5px;
    line-height: 1.45;
  }
  .doctor-name {
    color: var(--accent);
    font-weight: 600;
    font-size: 17px;
    line-height: 1.2;
  }
  .crm { margin-bottom: 12px; }
  .address { margin-bottom: 12px; }
  .contact-list { list-style: none; }
  .contact-list li { display: flex; align-items: center; gap: 8px; }
  .contact-icon { width: 11px; height: 11px; flex: none; }
  .contact-square {
    width: 9px; height: 9px; flex: none;
    background: var(--accent);
    margin: 0 1px;
  }
  /* back: brand side */
  .card--brand {
    display: flex;
    align-items: center;
    justify-content: center;
  }
  .brand-name {
    color: var(--accent);
    font-weight: 400;
    font-size: 34px;
    letter-spacing: 5px;
    text-align: center;
    line-height: 1.15;
  }
</style>
</head>
<body>
  <section class="card card--contact">
    <div class="mark-panel">
      <span class="mark-dot"></span>
      <span class="mark-name">LUMORA</span>
    </div>
    <div class="details">
      <p class="doctor-name">Doctor Name</p>
      <p class="crm">AB1241ABD</p>
      <p class="address">12345, Address Goes Here<br>Country Name, 123456</p>
      <ul class="contact-list">
        <li>
          <svg class="contact-icon" viewBox="0 0 24 24" aria-hidden="true"><path fill="#19c1e2" d="M6.6 10.8a15.1 15.1 0 0 0 6.6 6.6l2.2-2.2c.3-.3.7-.4 1-.2 1.1.4 2.3.6 3.6.6.6 0 1 .4 1 1V20c0 .6-.4 1-1 1C10.6 21 3 13.4 3 4c0-.6.4-1 1-1h3.5c.6 0 1 .4 1 1 0 1.3.2 2.5.6 3.6.1.3 0 .7-.2 1z"/></svg>
          (044)-456-7890
        </li>
        <li>
          <svg class="contact-icon" viewBox="0 0 24 24" aria-hidden="true"><rect x="2" y="5" width="20" height="14" rx="1.5" fill="#19c1e2"/><path d="M3 6l9 7 9-7" fill="none" stroke="#121213" stroke-width="1.8"/></svg>
          info@youremail.com
        </li>
        <li><span class="contact-square"></span>lumoraesteticaclinica</li>
        <li><span class="contact-square"></span>lumoraesteticaclinica</li>
      </ul>
    </div>
  </section>

  <section class="card card--brand">
    <p class="brand-name">LUMORA<br><span style="font-size:18px;letter-spacing:3px;">CIRURGIA PLÁSTICA</span></p>
  </section>
</body>
</html>
```